Torvane Partners Brochure Design

Design a brochure for Torvane Partners, with a focus on the three key areas of the business:
- Business Advisory (consulting);
- Turnaround;
- Business Valuations.

Details in relation to the above available at www.torvanepartners-example.com

The aim of the document is to have something which works in a digital and physical form. The brochure should have each of the above areas on a separate A4 page so as to enable them to be presented digitally as stand alone brochures. Alternative designs which achieve the same will be accepted, I.e. Multiple brochures, one for whole of business and one for each business area.

Should also have a brief bio on Peter Lindgrove and Torvane Partners, also on a separate page or included in separate brochures if this approach is taken.

Industry/Entity Type

Digital

Requirements
Must have
• Please ensure that design flows from website.

```html
<!DOCTYPE html>
<html lang="en">
<head>
<meta charset="utf-8">
<title>Torvane Partners Brochure – Business Valuations</title>
<link rel="stylesheet" href="https://fonts.googleapis.com/css2?family=Oswald:wght@400;500&family=Open+Sans:wght@400;600;700&display=swap">
<style>
  :root {
    --brand-blue: #0b5bd8;
    --brand-blue-dark: #0a4fbf;
    --accent-orange: #e5531a;
    --ink: #2b2b2b;
    --paper: #ffffff;
    --backdrop: #eef0f3;
    --photo-light: #c9d3dc;
    --photo-mid: #8e9aa6;
    --photo-dark: #4a525b;
  }
  * { box-sizing: border-box; margin: 0; padding: 0; }
  html, body {
    width: 1200px; height: 831px; overflow: hidden;
    background: var(--backdrop);
  }
  .spread {
    position: absolute; left: 63px; top: 35px;
    width: 1074px; height: 760px;
    display: flex;
  }
  .page { width: 537px; height: 760px; position: relative; overflow: hidden; }

  /* Left page */
  .page--valuations { background: var(--paper); }
  .hero-photo {
    position: absolute; left: 0; top: 0; width: 100%; height: 300px;
    background: linear-gradient(160deg, var(--photo-light) 0%, #aeb8c2 40%, var(--photo-mid) 70%, var(--photo-dark) 100%);
  }
  .title-band {
    position: absolute; left: 0; top: 272px; width: 100%; height: 66px;
    background: var(--brand-blue);
    padding: 6px 0 0 36px;
  }
  .title-band h1 {
    font-family: "Oswald", sans-serif; font-weight: 400;
    font-size: 42px; line-height: 52px; color: var(--paper);
  }
  .content { position: absolute; left: 36px; right: 34px; top: 352px; }
  .content h2 {
    font-family: "Oswald", sans-serif; font-weight: 500;
    font-size: 22px; color: var(--brand-blue); margin-bottom: 10px;
  }
  .content p, .content li {
    font-family: "Open Sans", sans-serif; font-size: 13.5px;
    line-height: 1.55; color: var(--ink);
  }
  .content p + p, .content .needs { margin-top: 14px; }
  .needs-list { margin: 2px 0 14px 46px; }
  .needs-list li { list-style: disc; }
  .folio-left {
    position: absolute; left: 36px; bottom: 22px;
    display: flex; align-items: center; gap: 8px;
    font-family: "Open Sans", sans-serif; font-weight: 700;
    font-size: 12px; color: var(--accent-orange);
  }
  .folio-left .marker { width: 6px; height: 16px; background: var(--brand-blue); }

  /* Right page */
  .page--partners { background: var(--brand-blue); }
  .partners {
    position: absolute; left: 0; right: 0; top: 150px;
    display: flex; flex-direction: column; align-items: center;
  }
  .partners h2 {
    font-family: "Oswald", sans-serif; font-weight: 400;
    font-size: 28px; color: var(--paper); margin-bottom: 30px;
  }
  .partner-list { list-style: none; display: flex; flex-direction: column; gap: 26px; align-items: center; }
  .partner {
    display: flex; align-items: center; gap: 10px;
    font-family: "Open Sans", sans-serif; font-weight: 700;
    font-size: 20px; color: var(--paper);
  }
  .partner .dot { width: 26px; height: 26px; border-radius: 50%; background: var(--paper); }
  .folio-right {
    position: absolute; right: 30px; bottom: 22px;
    font-family: "Open Sans", sans-serif; font-weight: 600;
    font-size: 11px; color: var(--paper);
  }
</style>
</head>
<body>
<main class="spread">
  <section class="page page--valuations">
    <div class="hero-photo" role="img" aria-label="Photo of business advisers discussing documents around a meeting table"></div>
    <div class="title-band"><h1>Business Valuations</h1></div>
    <div class="content">
      <h2>Experienced, trusted reporting for your company</h2>
      <p>With significant experience in business valuation across many businesses in Sydney, Torvane Partners tailors a valuation to suit your needs. We ensure that the reports are written in plain English and our methodology is fully explained. This enables the users to fully understand the process.</p>
      <p class="needs">We offer valuations for varied needs, including:</p>
      <ul class="needs-list">
        <li>Buying / Selling Business</li>
        <li>Family matters</li>
        <li>Partnership issues</li>
        <li>Divorce settlements</li>
        <li>Raising capital</li>
        <li>Business reorganisation</li>
        <li>Retirement planning</li>
      </ul>
      <p>For leading company valuations in Sydney or across NSW, trust the team of experts at Torvane Partners. Contact us today for more information.</p>
    </div>
    <div class="folio-left"><span class="marker"></span>10 | Torvane Partners</div>
  </section>

  <section class="page page--partners">
    <div class="partners">
      <h2>Our Partners</h2>
      <ul class="partner-list">
        <li class="partner"><span class="dot"></span>Guild of Chartered Auditors</li>
        <li class="partner">Brightsound</li>
        <li class="partner">Restora Alliance</li>
        <li class="partner">Watchkeep</li>
        <li class="partner"><span class="dot"></span>Ledgerly</li>
      </ul>
    </div>
    <div class="folio-right">Torvane Partners 11</div>
  </section>
</main>
</body>
</html>
```